Book Cover for Christian book about open-air preaching

The book is about open-air or outdoor preaching. It is for pastors, evangelists, or any Christian who feels called to share the Gospel with crowds outside of the church. The title is "Silver Lanterns" with a subtitle of "A guide to harbour-side singing in a restless era". The Bible verse reference for the title is Corvane 20:9. Size will be 9" high by 6"wide
Updates

Went on vacation/holiday

Target Market(s)

Christian pastors, missonaries, evangelists

Industry/Entity Type

religous

Requirements
Must have
• Meet Tarvelo Print Gateway guidelines for book covers

```html
<!DOCTYPE html>
<html lang="en">
<head>
<meta charset="utf-8">
<title>Silver Lanterns — Book Cover</title>
<link rel="stylesheet" href="https://fonts.googleapis.com/css2?family=Cinzel:wght@400;700&family=Uncial+Antiqua&display=swap">
<style>
  :root {
    --ink: #050302;
    --ember: #e8741c;
    --flame-hot: #ffb347;
    --sepia-light: #c9773a;
    --text: #ffffff;
    --emblem-glow: #e8862c;
  }
  html, body {
    margin: 0;
    padding: 0;
    overflow: hidden;
    background: var(--ink);
  }
  .cover {
    position: relative;
    width: 800px;
    height: 1200px;
    overflow: hidden;
    background: var(--ink);
  }
  .crowd-photo {
    position: absolute;
    left: 0;
    top: 0;
    width: 800px;
    height: 560px;
    background:
      radial-gradient(ellipse at 35% 40%, rgba(214,132,62,0.85) 0%, rgba(150,70,20,0.6) 40%, transparent 75%),
      linear-gradient(180deg, #6b2f0c 0%, var(--sepia-light) 35%, #7a3810 70%, var(--ink) 100%);
  }
  .flames-photo {
    position: absolute;
    left: 0;
    bottom: 0;
    width: 800px;
    height: 320px;
    background:
      radial-gradient(ellipse at 45% 85%, var(--flame-hot) 0%, var(--ember) 35%, rgba(180,50,10,0.6) 60%, transparent 85%),
      linear-gradient(0deg, #d9641a 0%, #8a2e08 45%, var(--ink) 100%);
  }
  .title {
    position: absolute;
    left: 0;
    top: 347px;
    width: 800px;
    margin: 0;
    text-align: center;
    font-family: "Uncial Antiqua", serif;
    font-weight: 400;
    font-size: 118px;
    line-height: 118px;
    color: var(--text);
    text-shadow:
      3px 4px 2px rgba(90,40,10,0.9),
      0 0 24px rgba(232,116,28,0.95),
      0 0 50px rgba(232,116,28,0.7);
  }
  .title span { display: block; }
  .verse-ref {
    position: absolute;
    left: 441px;
    top: 606px;
    margin: 0;
    font-family: "Cinzel", serif;
    font-weight: 400;
    font-size: 28px;
    line-height: 36px;
    color: var(--text);
    letter-spacing: 0.5px;
  }
  .emblem {
    position: absolute;
    left: 372px;
    top: 648px;
    width: 56px;
    height: 80px;
    background: radial-gradient(ellipse at 50% 45%, rgba(232,134,44,0.55) 0%, rgba(232,134,44,0.15) 50%, transparent 75%);
  }
  .subtitle {
    position: absolute;
    left: 0;
    top: 742px;
    width: 800px;
    margin: 0;
    text-align: center;
    font-family: "Cinzel", serif;
    color: var(--text);
  }
  .subtitle .lead,
  .subtitle .tail {
    display: block;
    font-weight: 400;
    font-size: 32px;
    line-height: 46px;
    letter-spacing: 1.5px;
  }
  .subtitle .focus {
    display: block;
    font-weight: 700;
    font-size: 40px;
    line-height: 50px;
    letter-spacing: 0.5px;
  }
</style>
</head>
<body>
  <main class="cover">
    <div class="crowd-photo" role="img" aria-label="Warm sepia-toned photo of a worshipping crowd with raised hands"></div>
    <div class="flames-photo" role="img" aria-label="Orange flames rising along the bottom edge with flying sparks"></div>

    <h1 class="title"><span>Silver</span><span>Lanterns</span></h1>

    <p class="verse-ref">Corvane 20:9</p>

    <div class="emblem" role="img" aria-label="Small glowing emblem above the subtitle"></div>

    <h2 class="subtitle">
      <span class="lead">A guide to</span>
      <span class="focus">HARBOUR-SIDE SINGING</span>
      <span class="tail">in a restless era</span>
    </h2>
  </main>
</body>
</html>
```